Beautiful collection of labels for unique hgh end food proucts

We are a online retailer of high end food and are looking for a design of 5 labels for our collection of products. Our products are quality, high end products Made in Italy by artisans. We want to create labels that are simple, elegant, modern and visually powerful. The labels will go on our boxes that are shiny chrome and strictly similar for most of our products. The labels are what differentiate one box from another and one product from another.

Reason: Merry Xmas to All

Target Market(s)

Consumers of High Quality Food Products

Industry/Entity Type

Online

Requirements
Must have
• Strong clear minimalist theme driven by patterns repeated throughot the series of labels

```html
<!DOCTYPE html>
<html lang="en">
<head>
<meta charset="utf-8">
<title>For My Friends – Label</title>
<link rel="stylesheet" href="https://fonts.googleapis.com/css2?family=Pinyon+Script&display=swap">
<style>
  :root {
    --paper: #ffffff;
    --ink: #111111;
    --pinwheel-tone: #7d7d7d;
    --petal-tone: #6a6a6a;
  }
  html, body {
    margin: 0;
    padding: 0;
    width: 1200px;
    height: 1200px;
    overflow: hidden;
    background: var(--paper);
  }
  .label {
    display: block;
    width: 1200px;
    height: 1200px;
  }
  .band { stroke: var(--ink); stroke-width: 2; }
  .band--pinwheel { fill: var(--pinwheel-tone); }
  .band--petal { fill: var(--petal-tone); }
  .seal__ring { fill: var(--paper); stroke: var(--ink); stroke-width: 9; }
  .seal__inner { fill: none; stroke: var(--ink); stroke-width: 2.5; }
  .seal__title {
    font-family: "Pinyon Script", cursive;
    fill: var(--ink);
    font-size: 108px;
  }
</style>
</head>
<body>
<svg class="label" viewBox="0 0 1200 1200" xmlns="http://www.w3.org/2000/svg">
  <g class="bands">
    <rect class="band band--pinwheel" x="174" y="-2" width="851" height="116" role="img" aria-label="Black and white pinwheel triangle pattern band"/>
    <rect class="band band--petal" x="174" y="152" width="851" height="116" role="img" aria-label="Black and white interlocking circle petal pattern band"/>
    <rect class="band band--pinwheel" x="174" y="308" width="851" height="116" role="img" aria-label="Black and white pinwheel triangle pattern band"/>
    <rect class="band band--petal" x="174" y="462" width="851" height="116" role="img" aria-label="Black and white interlocking circle petal pattern band"/>
    <rect class="band band--pinwheel" x="174" y="618" width="851" height="116" role="img" aria-label="Black and white pinwheel triangle pattern band"/>
    <rect class="band band--petal" x="174" y="772" width="851" height="116" role="img" aria-label="Black and white interlocking circle petal pattern band"/>
    <rect class="band band--pinwheel" x="174" y="928" width="851" height="116" role="img" aria-label="Black and white pinwheel triangle pattern band"/>
    <rect class="band band--petal" x="174" y="1082" width="851" height="116" role="img" aria-label="Black and white interlocking circle petal pattern band"/>
  </g>
  <g class="seal">
    <circle class="seal__ring" cx="598" cy="594" r="252"/>
    <circle class="seal__inner" cx="598" cy="594" r="236"/>
    <g transform="rotate(-6 598 594)">
      <text class="seal__title" x="598" y="566" text-anchor="middle">For My</text>
      <text class="seal__title" x="610" y="674" text-anchor="middle">Friends</text>
    </g>
  </g>
</svg>
</body>
</html>
```